Need CATCHY/VIVID Banner design for my new UTV/ATV/Off Road Vehicle turn signal/lighting company

I need a banner ad designed so I can advertise on several different ATV (all terrain vehicle), UTV (Utility Vehicles), Golf Cart and Off-Road Vehicle forums. Ads need to be very catchy and produce a call to action. Action is getting hits to my website. Our main business is selling turn signal kits to make your side by side or your ATV/UTV street legal, as some states now allow you to drive these on public roads if you have the following items: Turn Signals, Horn, Lighted license plate bracket, headlights and brake lights. We sell all of these items for just about any model vehicle out there. Our call to action for this banner would be to get more website visits.

Target Market(s)

Off-road/outdoor enthusiasts,

Industry/Entity Type

Car Accessorie

Font styles to use
Sans Serif

Requirements
Must have
• Ad size need to be either 728x90 or 300x250. Colorful ad with an off-road vehicle integrated to the design (think UTV, side-by-side, etc.
Nice to have
• Nice to haves would be anything that makes this banner ad stand out on very boring web pages.
Should not have
• anything dull

```html
<!DOCTYPE html>
<html lang="en">
<head>
<meta charset="UTF-8">
<title>ATV &amp; UTV Signal Lighting Banner</title>
<link href="https://fonts.googleapis.com/css2?family=Montserrat:wght@700;800;900&display=swap" rel="stylesheet">
<style>
  :root {
    --white: #ffffff;
    --ink: #111111;
    --red: #e5202a;
    --amber: #f5a51c;
    --yellow: #f7c21b;
    --pink: #f6a2a6;
    --blush: #fbd3d5;
  }
  html, body {
    margin: 0;
    padding: 0;
    width: 1200px;
    height: 1000px;
    overflow: hidden;
    background: var(--white);
  }
  .banner {
    position: relative;
    width: 1200px;
    height: 1000px;
    background: var(--white);
    font-family: "Montserrat", Arial, sans-serif;
    overflow: hidden;
  }
  .backdrop {
    position: absolute;
    inset: 0;
    width: 1200px;
    height: 1000px;
  }
  .brand {
    position: absolute;
    left: 74px;
    top: 150px;
    display: flex;
    align-items: center;
    gap: 18px;
  }
  .brand-mark {
    width: 42px;
    height: 42px;
    background: var(--red);
  }
  .brand-name {
    font-weight: 800;
    font-size: 40px;
    letter-spacing: 1px;
    color: var(--ink);
    line-height: 1;
  }
  .headline {
    position: absolute;
    left: 66px;
    top: 448px;
    margin: 0;
    font-weight: 800;
    line-height: 1;
    text-transform: uppercase;
  }
  .headline span { display: block; }
  .headline-top {
    font-size: 84px;
    color: var(--amber);
    letter-spacing: 1px;
  }
  .headline-mid {
    font-size: 84px;
    color: var(--red);
    margin-top: 8px;
    letter-spacing: 1px;
  }
  .headline-sub {
    font-size: 47px;
    color: var(--ink);
    margin-top: 18px;
  }
  .tagline {
    position: absolute;
    left: 70px;
    top: 728px;
    margin: 0;
    font-weight: 800;
    font-size: 33px;
    line-height: 1.2;
    color: var(--ink);
    text-transform: uppercase;
  }
  .feature-icons {
    position: absolute;
    left: 64px;
    top: 858px;
    display: flex;
    gap: 56px;
    align-items: center;
  }
  .feature-icons svg { display: block; }
</style>
</head>
<body>
<div class="banner">
  <svg class="backdrop" viewBox="0 0 1200 1000" xmlns="http://www.w3.org/2000/svg">
    <defs>
      <linearGradient id="terrain" x1="0" y1="0" x2="0" y2="1">
        <stop offset="0" stop-color="#9fb8c9"/>
        <stop offset="0.18" stop-color="#b9a98f"/>
        <stop offset="0.45" stop-color="#4a3b34"/>
        <stop offset="0.7" stop-color="#2a2324"/>
        <stop offset="1" stop-color="#b38d64"/>
      </linearGradient>
    </defs>
    <!-- chevron bands -->
    <polygon class="band-blush" points="650,0 1200,0 1200,1000 760,1000 520,560" fill="var(--blush)"/>
    <polygon class="band-pink" points="690,0 1200,0 1200,1000 790,1000 560,560" fill="var(--pink)"/>
    <polygon class="band-red" points="720,0 1200,0 1200,1000 820,1000 590,560" fill="var(--red)"/>
    <polygon class="band-yellow" points="760,0 1200,0 1200,1000 860,1000 630,560" fill="var(--yellow)"/>
    <polygon class="band-amber" points="790,0 1200,0 1200,1000 890,1000 660,560" fill="var(--amber)"/>
    <!-- vehicle photo area -->
    <polygon class="photo" points="810,0 1200,0 1200,1000 910,1000 680,560" fill="url(#terrain)" role="img" aria-label="Photo of a black off-road side-by-side UTV with red roll cage on desert terrain with mountains behind"/>
  </svg>

  <div class="brand">
    <div class="brand-mark"></div>
    <div class="brand-name">TRAILMARK SIGNAL CO.</div>
  </div>

  <h1 class="headline">
    <span class="headline-top">ATV &amp; UTV</span>
    <span class="headline-mid">Vechicle</span>
    <span class="headline-sub">Signal Lighting</span>
  </h1>

  <p class="tagline">Off Road Vehicle<br>Turn Signal</p>

  <div class="feature-icons">
    <svg width="72" height="60" viewBox="0 0 72 60" aria-label="Brake light">
      <circle cx="36" cy="30" r="20" fill="none" stroke="var(--red)" stroke-width="5"/>
      <path d="M10 12 A30 30 0 0 0 10 48 M62 12 A30 30 0 0 1 62 48" fill="none" stroke="var(--red)" stroke-width="5" stroke-linecap="round"/>
      <rect x="33" y="17" width="6" height="17" rx="2" fill="var(--red)"/>
      <circle cx="36" cy="41" r="3.5" fill="var(--red)"/>
    </svg>
    <svg width="76" height="60" viewBox="0 0 76 60" aria-label="Headlight">
      <g stroke="var(--red)" stroke-width="5" stroke-linecap="round">
        <line x1="4" y1="16" x2="22" y2="16"/>
        <line x1="4" y1="30" x2="22" y2="30"/>
        <line x1="4" y1="44" x2="22" y2="44"/>
      </g>
      <path d="M42 8 C66 8 72 20 72 30 C72 40 66 52 42 52 Z" fill="var(--red)"/>
      <rect x="30" y="8" width="14" height="44" fill="var(--red)"/>
    </svg>
    <svg width="86" height="60" viewBox="0 0 86 60" aria-label="Horn">
      <path d="M6 24 H22 L60 8 V52 L22 36 H6 Z" fill="var(--red)"/>
      <rect x="18" y="36" width="8" height="12" fill="var(--red)"/>
      <g stroke="var(--red)" stroke-width="4" stroke-linecap="round">
        <line x1="68" y1="18" x2="80" y2="12"/>
        <line x1="68" y1="30" x2="82" y2="30"/>
        <line x1="68" y1="42" x2="80" y2="48"/>
      </g>
    </svg>
    <svg width="96" height="60" viewBox="0 0 96 60" aria-label="Turn signals">
      <path d="M30 8 L6 30 L30 52 V40 H44 V20 H30 Z" fill="none" stroke="var(--red)" stroke-width="5" stroke-linejoin="round"/>
      <path d="M66 8 L90 30 L66 52 V40 H52 V20 H66 Z" fill="none" stroke="var(--red)" stroke-width="5" stroke-linejoin="round"/>
    </svg>
  </div>
</div>
</body>
</html>
```